Industrial Design Business Card

I am an industrial designer that needs a nice business card that gives a sense of my personal brand (the work I do, how I'm different than others though subtle design). Since I am a designer, myself, the business card needs to have an impeccable design, while feeling like it represents me. Please see the link to my portfolio where you can get a better sense for me.

http://www.markdpelletier.example/

Target Market(s)

Potential employers, industrial designers

Industry/Entity Type

Business

Contact Information for Business Card

Mark Pelletier
Industrial Designer
markpelletierdesign.example
markpelletierdesign@mailbox.example
(555) 218-4370

Font styles to use
Sans Serif

Colors

Designer to choose colors to be used in the design.

Requirements
Must have
• Must have all of the business card details - ideally in that order. If it will look better in a different order, that's fine.
• Simple design - not too flashy. Using a font that is not a pre-set will likely be key to making this simple but also stand out. But also keep somewhat consistent with the fonts and look of my portfolio (markpelletierdesign.example).
• It needs to catch someone's attention while also being simple (not too flashy) design. That is the big challenge.
Should not have
• Random pictures off the internet.

```html
<!DOCTYPE html>
<html lang="en">
<head>
<meta charset="utf-8">
<title>Mark Pelletier — Business Card</title>
<link rel="stylesheet" href="https://fonts.googleapis.com/css2?family=Mulish:wght@400;500&family=Open+Sans:wght@600&display=swap">
<style>
  :root {
    --page-bg: #e4e4e5;
    --card-front: #ffffff;
    --card-back: #626365;
    --ink: #111111;
    --ink-soft: #6b6b6b;
    --rule: #333333;
    --name-on-dark: #ffffff;
  }
  * { box-sizing: border-box; margin: 0; padding: 0; }
  html, body {
    width: 1200px; height: 1200px; overflow: hidden;
    background: var(--page-bg);
  }
  .sheet {
    width: 1200px; height: 1200px;
    display: flex; flex-direction: column; align-items: center; justify-content: center;
    gap: 60px;
  }
  .card {
    position: relative;
    width: 900px; height: 508px;
    box-shadow: 4px 6px 14px rgba(0,0,0,0.35);
  }
  .card--front { background: var(--card-front); }
  .card--back {
    background: var(--card-back);
    display: flex; align-items: center; justify-content: center;
  }
  .identity {
    position: absolute; left: 0; right: 0; top: 142px;
    text-align: center;
  }
  .identity__name {
    font-family: "Open Sans", sans-serif; font-weight: 600;
    font-size: 41px; color: var(--ink); letter-spacing: 0.2px; line-height: 1.1;
  }
  .identity__role {
    font-family: "Mulish", sans-serif; font-weight: 400;
    font-size: 24px; color: var(--ink-soft); margin-top: 4px;
  }
  .contact {
    position: absolute; top: 388px; transform: translateX(-50%);
    text-align: center;
    font-family: "Mulish", sans-serif; font-weight: 500;
    font-size: 22px; line-height: 1.3; color: var(--ink);
    white-space: nowrap;
  }
  .contact__icon { display: block; margin: 0 auto 12px; width: 30px; height: 30px; }
  .contact--phone { left: 158px; }
  .contact--email { left: 412px; }
  .contact--web { left: 725px; }
  .divider {
    position: absolute; top: 378px; width: 1.5px; height: 102px; background: var(--rule);
  }
  .divider--first { left: 272px; }
  .divider--second { left: 554px; }
  .back-name {
    font-family: "Open Sans", sans-serif; font-weight: 600;
    font-size: 42px; color: var(--name-on-dark); letter-spacing: 0.3px;
  }
</style>
</head>
<body>
<main class="sheet">
  <section class="card card--front" aria-label="Card front">
    <div class="identity">
      <h1 class="identity__name">Mark Pelletier</h1>
      <p class="identity__role">Industrial Designer</p>
    </div>

    <div class="contact contact--phone">
      <svg class="contact__icon" viewBox="0 0 24 24" aria-hidden="true">
        <path fill="#111" d="M6.6 10.8a15.1 15.1 0 0 0 6.6 6.6l2.2-2.2c.3-.3.7-.4 1-.2 1.1.4 2.3.6 3.6.6.6 0 1 .4 1 1V20c0 .6-.4 1-1 1A17 17 0 0 1 3 4c0-.6.4-1 1-1h3.5c.6 0 1 .4 1 1 0 1.3.2 2.5.6 3.6.1.3 0 .7-.2 1z"/>
      </svg>
      <span>(555) 218-4370</span>
    </div>

    <span class="divider divider--first"></span>

    <div class="contact contact--email">
      <svg class="contact__icon" viewBox="0 0 24 24" aria-hidden="true">
        <rect x="2" y="5" width="20" height="14" rx="1" fill="#111"/>
        <path d="M2.5 5.8 12 13l9.5-7.2" fill="none" stroke="#fff" stroke-width="1.6"/>
      </svg>
      <span>markpelletierdesign<br>@mailbox.example</span>
    </div>

    <span class="divider divider--second"></span>

    <div class="contact contact--web">
      <svg class="contact__icon" viewBox="0 0 24 24" aria-hidden="true">
        <g fill="none" stroke="#111" stroke-width="2.6" stroke-linecap="round">
          <path d="M10.5 13.5a4 4 0 0 0 5.7 0l3-3a4 4 0 0 0-5.7-5.7l-1.3 1.3"/>
          <path d="M13.5 10.5a4 4 0 0 0-5.7 0l-3 3a4 4 0 0 0 5.7 5.7l1.3-1.3"/>
        </g>
      </svg>
      <span>markpelletierdesign.example</span>
    </div>
  </section>

  <section class="card card--back" aria-label="Card back">
    <p class="back-name">Mark Pelletier</p>
  </section>
</main>
</body>
</html>
```